Our companies name is The Gilded Ladle and we specialize in craft cupcakes, what I mean by that is that we bake our cupcakes with craft beer and other alcoholic drinks. We are trying to focus on being elegant but at the same time unpretentious. Since we are incorporating beer in our cupcakes we want the business card to have our logo in the front and our information in the back.

Once we select the best design we will provide the contact information to be added. Thank you.

Industry/Entity Type

Business

Font styles to use
Decorative
Script

Requirements
Must have
• Round corners
Should not have
• Square corners

```html
<!DOCTYPE html>
<html lang="en">
<head>
<meta charset="utf-8">
<title>The Gilded Ladle – Business Card</title>
<link href="https://fonts.googleapis.com/css2?family=Rye&family=Tinos&family=Pirata+One&display=swap" rel="stylesheet">
<style>
  :root {
    --stage: #3a3a3a;
    --card-black: #0b0b0b;
    --card-red: #d71f27;
    --teal: #8fd3c8;
    --paper: #f1ece4;
    --ink: #140a0a;
  }
  * { box-sizing: border-box; margin: 0; padding: 0; }
  html, body { width: 1200px; height: 900px; overflow: hidden; }
  body {
    background: var(--stage);
    position: relative;
  }
  .card {
    position: absolute;
    left: 280px;
    width: 640px;
    height: 366px;
    border-radius: 28px;
    overflow: hidden;
    background: var(--card-black);
  }
  .card--front { top: 60px; }
  .card--back { top: 474px; background: var(--card-red); }

  .brand-name {
    font-family: "Tinos", serif;
    font-weight: 400;
    color: var(--paper);
    text-align: center;
    line-height: 1.15;
  }
  .card--front .brand-name {
    position: absolute;
    inset: 0;
    display: flex;
    align-items: center;
    justify-content: center;
    font-size: 44px;
  }
  .card-back-shape { position: absolute; inset: 0; width: 100%; height: 100%; }
  .card--back .brand-name {
    position: absolute;
    left: 0;
    top: 0;
    width: 260px;
    height: 366px;
    display: flex;
    align-items: center;
    justify-content: center;
    font-size: 30px;
    padding: 0 24px;
  }
  .contact {
    position: absolute;
    left: 290px;
    right: 20px;
    top: 70px;
    color: var(--ink);
    text-align: center;
  }
  .contact__name {
    font-family: "Rye", serif;
    font-weight: 400;
    font-size: 34px;
    letter-spacing: 1px;
    padding-bottom: 6px;
    border-bottom: 3px dotted var(--ink);
    display: inline-block;
  }
  .contact__value {
    font-family: "Tinos", serif;
    margin-top: 26px;
    font-size: 25px;
    line-height: 1;
  }
  .contact__value--email { margin-top: 16px; font-size: 20px; }
  .contact__label {
    font-family: "Pirata One", serif;
    font-size: 17px;
    letter-spacing: 1px;
    line-height: 1.1;
  }
</style>
</head>
<body>
  <section class="card card--front" aria-label="Card front">
    <h1 class="brand-name">The Gilded Ladle</h1>
  </section>

  <section class="card card--back" aria-label="Card back">
    <svg class="card-back-shape" viewBox="0 0 640 366" preserveAspectRatio="none" aria-hidden="true">
      <path fill="#0b0b0b" d="M0 0 L260 0 Q270 7.5 260 15 T260 30 T260 45 T260 60 T260 75 T260 90 T260 105 T260 120 T260 135 T260 150 T260 165 T260 180 T260 195 T260 210 T260 225 T260 240 T260 255 T260 270 T260 285 T260 300 T260 315 T260 330 T260 345 T260 360 T260 375 L0 375 Z"/>
      <path fill="none" stroke="#8fd3c8" stroke-width="3" d="M260 0 Q270 7.5 260 15 T260 30 T260 45 T260 60 T260 75 T260 90 T260 105 T260 120 T260 135 T260 150 T260 165 T260 180 T260 195 T260 210 T260 225 T260 240 T260 255 T260 270 T260 285 T260 300 T260 315 T260 330 T260 345 T260 360 T260 375"/>
    </svg>
    <p class="brand-name">The Gilded Ladle</p>
    <div class="contact">
      <h2 class="contact__name">ROSA DELGADO</h2>
      <p class="contact__value">[555] 013-4827</p>
      <p class="contact__label">phone</p>
      <p class="contact__value contact__value--email">thegildedladle@example.com</p>
      <p class="contact__label">email</p>
    </div>
  </section>
</body>
</html>
```